real esate business card with company logo and name

we need a business card design for a real esate company

The company name is Walsh & Ortiz Pty Ltd, and we have our logo designed and will upload. We want classic or moden feel. Black or white background. looks more textured. Should include folowinginformations
Paul Walsh and Tara Ortiz
Sales Agents & Onsite Manager
p: 07 5948 2610
F: 07 5948 2795
M:0451 786 923
3/22 Marlow Crescent, BRAMBLE PARK QLD 4512

We want this business card looks professonal. Thank you in advance.

Industry/Entity Type

Real Estate Agent

Contact Information for Business Card

Paul Walsh and Tara Ortiz
Onsite Manager & Sales Agents
p: 07 5948 2610
M:0451 786 923

Font styles to use
Serif

Colors
000000
fbfbfb
333333
959595

Requirements
Must have
• company logo and name, black or white back ground

```html
<!DOCTYPE html>
<html lang="en">
<head>
<meta charset="utf-8">
<title>Walsh &amp; Ortiz Pty Ltd — Business Card</title>
<link href="https://fonts.googleapis.com/css2?family=Roboto+Condensed:wght@400;500&family=Source+Sans+3:wght@400&display=swap" rel="stylesheet">
<style>
  :root {
    --stage: #a9a7a8;
    --card: #fbfbfb;
    --ink-dark: #505359;
    --ink-mid: #7b7c80;
    --ink-soft: #a0a0a4;
    --swoosh: #c9c9cd;
    --band: #50535a;
  }
  * { margin: 0; padding: 0; box-sizing: border-box; }
  html, body { width: 1200px; height: 1200px; overflow: hidden; }
  body { background: var(--stage); position: relative; font-family: "Source Sans 3", sans-serif; }

  .card {
    position: absolute;
    background: var(--card);
    border-radius: 24px;
    overflow: hidden;
  }
  .card--front { left: 238px; top: 120px; width: 712px; height: 410px; }
  .card--back  { left: 230px; top: 645px; width: 722px; height: 415px; }

  .brand-mark {
    position: absolute;
    background: var(--ink-mid);
  }
  .card--front .brand-mark { width: 70px; height: 70px; left: 321px; top: 150px; }
  .card--back .brand-mark  { width: 70px; height: 70px; left: 528px; top: 225px; }

  .brand-name {
    position: absolute;
    font-family: "Roboto Condensed", sans-serif;
    font-weight: 400;
    color: var(--ink-mid);
    letter-spacing: 0.5px;
    text-transform: uppercase;
    white-space: nowrap;
  }
  .card--front .brand-name { left: 0; right: 0; top: 288px; text-align: center; font-size: 25px; }
  .card--back .brand-name  { right: 52px; top: 355px; font-size: 23px; }

  .band { position: absolute; left: 0; top: 0; width: 722px; height: 180px; }

  .agents {
    position: absolute; left: 48px; top: 116px;
    font-family: "Roboto Condensed", sans-serif;
    font-size: 27px; font-weight: 400; color: var(--ink-dark);
  }
  .role {
    position: absolute; left: 48px; top: 157px;
    font-family: "Roboto Condensed", sans-serif;
    font-size: 14.5px; color: var(--ink-dark);
  }
  .contacts { position: absolute; left: 48px; top: 244px; list-style: none; }
  .contacts li {
    display: flex; align-items: center; height: 27px;
    font-size: 17px; color: var(--ink-dark);
  }
  .contacts svg { width: 18px; height: 18px; margin-right: 16px; fill: var(--ink-soft); }
  .address {
    position: absolute; left: 48px; top: 330px;
    font-size: 17px; line-height: 28px; color: var(--ink-dark); font-style: normal;
  }
</style>
</head>
<body>

<section class="card card--front" aria-label="Card front">
  <div class="brand-mark"></div>
  <p class="brand-name">Walsh &amp; Ortiz Pty Ltd.</p>
</section>

<section class="card card--back" aria-label="Card back">
  <svg class="band" viewBox="0 0 722 180" aria-hidden="true">
    <path d="M0,0 H722 V150 C600,140 520,80 300,30 C200,10 80,15 0,25 Z" fill="var(--band)"/>
    <path d="M0,25 C80,15 200,10 300,30 C520,80 600,140 722,150 V160 C600,152 500,100 300,52 C200,36 100,36 0,46 Z" fill="var(--swoosh)"/>
  </svg>

  <h1 class="agents">Paul Walsh &amp; Tara Ortiz</h1>
  <p class="role">Sales Agents &amp; Onsite Manager</p>

  <ul class="contacts">
    <li>
      <svg viewBox="0 0 18 18" aria-label="Mobile"><path d="M5 1h8a1 1 0 0 1 1 1v14a1 1 0 0 1-1 1H5a1 1 0 0 1-1-1V2a1 1 0 0 1 1-1zm.8 2v10.5h6.4V3zM9 14.3a.9.9 0 1 0 0 1.8.9.9 0 0 0 0-1.8z"/></svg>
      0451 786 923
    </li>
    <li>
      <svg viewBox="0 0 18 18" aria-label="Phone"><path d="M1 6c2-3 14-3 16 0l-1 2-3-1V5.5C11 5 7 5 5 5.5V7L2 8zM4 9h10l2 6H2zm5 1.5a2 2 0 1 0 0 4 2 2 0 0 0 0-4z"/></svg>
      07 5948 2610
    </li>
    <li>
      <svg viewBox="0 0 18 18" aria-label="Fax"><path d="M5 1h8v5H5zM2 7h14a1 1 0 0 1 1 1v6H1V8a1 1 0 0 1 1-1zm3 8h8v2H5zm9-6a1 1 0 1 0 0 2 1 1 0 0 0 0-2z"/></svg>
      07 5948 2795
    </li>
  </ul>

  <address class="address">3/22 Marlow Crescent,<br>BRAMBLE PARK QLD 4512</address>

  <div class="brand-mark"></div>
  <p class="brand-name">Walsh &amp; Ortiz Pty Ltd.</p>
</section>

</body>
</html>
```